Introduction brochure for IT Company

We need a brochure for introducing our new small business services to the market.

We need a template that we can alter and play with as services change, and was thinking about the following:

A front page which has logo (attached), and follows colour scheme used on our website www.quillotech.com.au, that has a small description of the service/or us, we are introducing and Call us on 1300 627 398 at the bottom of page.
For the first print only front page and back page will be used, as we are still refining the service. We will be introducing the company to new prospects face to face and want to leave them with a small brochure which explains what we do for them, and clear contact details.

Middle section we have not worked out fully yet, as it depends on space available, but please use points under service on our website for now to fill in with some points.

Last page we want to have the last 1/3 of page to be our contact details along with a google map of our location etc. like the contact us page on website.

We prefer to stay on the lighter side, so more playful in style but you guys are the experts.

Target Market(s)

Small business 1-10 Employees

Industry/Entity Type

It Company

Font styles to use
Serif

Requirements
Must have
• Clear contact details, playful design which is easy to read. Follow colour scheme or close to website, www.quillotech.com.au, as this is reflected in all our marketing. Some artistic license is of course given.
Nice to have
• Nothing comes to mind, go crazy and make it fun.
Should not have
• typical images of large scale server racks and enterprise level images. Stay small business.

```html
<!DOCTYPE html>
<html lang="en">
<head>
<meta charset="utf-8">
<title>Quillotech Brochure Spread</title>
<link href="https://fonts.googleapis.com/css2?family=Open+Sans:wght@400;600;700&family=Oswald:wght@500;700&display=swap" rel="stylesheet">
<style>
  :root {
    --red: #e31e24;
    --charcoal: #232323;
    --charcoal-soft: #3a3a3a;
    --ink: #111111;
    --paper: #ffffff;
    --backdrop: #e6e6e6;
    --grey-band: #e9e9e9;
  }
  * { box-sizing: border-box; margin: 0; padding: 0; }
  html, body { width: 1200px; height: 1200px; overflow: hidden; }
  body {
    background: var(--backdrop);
    font-family: "Open Sans", Arial, sans-serif;
    position: relative;
  }
  .spread {
    position: absolute;
    left: 60px; top: 250px;
    width: 1080px; height: 700px;
    display: flex;
    box-shadow: 0 12px 30px rgba(0,0,0,0.18);
  }
  .page {
    position: relative;
    width: 540px; height: 700px;
    background: var(--paper);
    overflow: hidden;
  }
  .page-art { position: absolute; inset: 0; }

  /* Back page */
  .contact { position: absolute; left: 56px; top: 38px; color: #fff; }
  .contact-title {
    font-weight: 700; font-size: 15px; color: var(--red);
    text-decoration: underline; letter-spacing: 0.5px; margin-bottom: 8px;
  }
  .contact-line { display: flex; align-items: center; gap: 8px; font-size: 11.5px; line-height: 17px; }
  .contact-line svg { width: 10px; height: 10px; flex: none; }

  .services {
    position: absolute; left: 70px; top: 150px;
    width: 400px; height: 250px;
    border: 1.5px solid rgba(255,255,255,0.55);
    border-radius: 26px;
    display: grid; grid-template-columns: 1fr 1fr;
    padding: 22px 24px;
    gap: 16px 20px;
  }
  .service { color: #e8e8e8; font-size: 12px; line-height: 14px; }
  .service svg { width: 52px; height: 40px; display: block; margin: 0 0 8px 30px; }

  .hardware-visual {
    position: absolute; left: 88px; top: 450px;
    width: 190px; height: 170px;
    background: linear-gradient(160deg, #4a4f57 0%, #111 70%);
    border-radius: 6px;
  }
  .location-map {
    position: absolute; left: 300px; top: 490px;
    width: 200px; height: 200px; border-radius: 50%;
    border: 8px solid var(--red);
    background: radial-gradient(circle at 45% 45%, #f3efe6 0%, #e4e1da 60%, #d6d2c8 100%);
  }

  /* Front page */
  .wordmark {
    position: absolute; right: 40px; top: 52px;
    display: flex; align-items: center; gap: 10px;
    font-family: "Oswald", Arial, sans-serif; font-weight: 700;
    font-size: 44px; color: var(--red); letter-spacing: 1px;
  }
  .wordmark-dot { width: 20px; height: 20px; background: var(--red); border-radius: 50%; }
  .family-photo {
    position: absolute; left: 36px; top: 140px;
    width: 504px; height: 330px;
    background: linear-gradient(120deg, #f7f3ee 0%, #e9d6c4 45%, #f5f5f5 100%);
  }
  .headline {
    position: absolute; left: 60px; top: 530px; right: 40px;
    font-family: "Oswald", Arial, sans-serif; text-transform: uppercase;
  }
  .headline-top { font-size: 36px; font-weight: 500; color: var(--ink); line-height: 44px; }
  .headline-main { font-size: 52px; font-weight: 700; color: var(--red); line-height: 58px; }
  .web-bar {
    position: absolute; left: 60px; right: 40px; top: 650px;
    height: 22px; background: var(--red); color: #fff;
    font-size: 12px; font-weight: 600; letter-spacing: 6px;
    display: flex; align-items: center; justify-content: center;
  }
</style>
</head>
<body>
  <main class="spread">
    <!-- Back page -->
    <section class="page page-back">
      <svg class="page-art" viewBox="0 0 540 700" aria-hidden="true">
        <defs>
          <linearGradient id="darkFill" x1="0" y1="0" x2="1" y2="1">
            <stop offset="0" stop-color="#2e2e2e"/>
            <stop offset="1" stop-color="#1b1b1b"/>
          </linearGradient>
        </defs>
        <path d="M0 0 H540 V600 C470 640 420 670 300 670 C170 670 90 600 40 560 C20 545 10 540 0 540 Z" fill="url(#darkFill)"/>
        <path d="M0 540 C10 540 20 545 40 560 C90 600 170 670 300 670 C420 670 470 640 540 600" fill="none" stroke="#e31e24" stroke-width="14"/>
      </svg>

      <div class="contact">
        <h2 class="contact-title">CONTACT US</h2>
        <p class="contact-line"><svg viewBox="0 0 10 10"><path d="M2 0 L4 2 L3 3.5 C4 5.5 5 6.5 6.5 7 L8 6 L10 8 L8 10 C4 10 0 6 0 2 Z" fill="#e31e24"/></svg>Phone: 1300 627 398</p>
        <p class="contact-line"><svg viewBox="0 0 10 10"><rect x="0" y="2" width="10" height="7" fill="#e31e24"/><path d="M0 2 L5 6 L10 2" stroke="#fff" fill="none"/></svg>Email: service@quillotech.com.au</p>
        <p class="contact-line"><svg viewBox="0 0 10 10"><path d="M5 0 L10 5 H8.5 V10 H1.5 V5 H0 Z" fill="#e31e24"/></svg>Address: 4/18 Harbour Lane, Bellmont TAS 7019</p>
        <p class="contact-line"><svg viewBox="0 0 10 10"><circle cx="5" cy="5" r="4.2" fill="none" stroke="#e31e24" stroke-width="1.4"/><path d="M5 2.5 V5 H7" stroke="#e31e24" fill="none"/></svg>Hours: Monday-Friday 9am - 5pm</p>
      </div>

      <div class="services">
        <div class="service">
          <svg viewBox="0 0 52 40"><path d="M8 20 L26 6 L44 20 V36 H8 Z" fill="#d9d9d9"/><path d="M4 21 L26 3 L48 21" stroke="#999" stroke-width="3" fill="none"/><rect x="22" y="24" width="8" height="12" fill="#777"/></svg>
          Residential computer<br>/ network issues
        </div>
        <div class="service">
          <svg viewBox="0 0 52 40"><circle cx="26" cy="9" r="7" fill="#6aa9e0"/><path d="M26 16 V24 M10 24 H42 M10 24 V28 M42 24 V28 M26 24 V28" stroke="#8fc3ee" stroke-width="2"/><rect x="2" y="28" width="16" height="10" fill="#3d8ad6"/><rect x="18" y="28" width="16" height="10" fill="#3d8ad6"/><rect x="34" y="28" width="16" height="10" fill="#3d8ad6"/></svg>
          Business computer<br>/ network issues
        </div>
        <div class="service">
          <svg viewBox="0 0 52 40"><path d="M2 22 L16 10 L30 22 V36 H2 Z" fill="#e6e6e6"/><rect x="24" y="12" width="24" height="16" fill="#3d8ad6"/><rect x="22" y="28" width="28" height="3" fill="#aaa"/></svg>
          Home<br>Networking
        </div>
        <div class="service">
          <svg viewBox="0 0 52 40"><path d="M12 24 L28 10 L44 24 V38 H12 Z" fill="#e6e6e6"/><circle cx="22" cy="20" r="9" fill="#3d6fc0"/><circle cx="22" cy="20" r="4" fill="#a9c8f0"/></svg>
          New Home<br>networking
        </div>
      </div>

      <div class="hardware-visual" role="img" aria-label="Glossy black desktop computer towers"></div>
      <div class="location-map" role="img" aria-label="Street map showing the office location with a red pin"></div>
    </section>

    <!-- Front page -->
    <section class="page page-front">
      <svg class="page-art" viewBox="0 0 540 700" aria-hidden="true">
        <defs>
          <linearGradient id="greyFill" x1="0" y1="0" x2="0" y2="1">
            <stop offset="0" stop-color="#dcdcdc"/>
            <stop offset="0.5" stop-color="#f6f6f6"/>
            <stop offset="1" stop-color="#ffffff"/>
          </linearGradient>
        </defs>
        <path d="M0 470 C150 455 330 440 540 490 V700 H0 Z" fill="url(#greyFill)"/>
        <path d="M0 470 C150 455 330 440 540 490" fill="none" stroke="#e31e24" stroke-width="8"/>
        <path d="M0 0 H110 C55 60 30 180 30 330 C30 400 34 440 40 480 L0 480 Z" fill="#e31e24"/>
        <path d="M0 0 H90 C45 60 18 180 18 330 C18 400 20 440 24 480 L0 480 Z" fill="#ffffff" opacity="0"/>
        <path d="M0 0 H60 C25 70 10 190 10 330 L10 480 H0 Z" fill="#ffffff"/>
      </svg>

      <div class="wordmark"><span class="wordmark-dot"></span>QUILLOTECH</div>
      <div class="family-photo" role="img" aria-label="Photo of a smiling family gathered around a laptop at home"></div>

      <div class="headline">
        <p class="headline-top">Your one stop shop for</p>
        <p class="headline-main">All your IT needs</p>
      </div>
      <div class="web-bar">www.quillotech.com.au</div>
    </section>
  </main>
</body>
</html>
```